Aisle Bloom Bridal Show Flyer

I need designed a reusable flyer that is more eye catching than my current flyer. I would also need separate layers as the details change from show to show. I attached the flyer I currently use.

Industry/Entity Type

Wedding

```html
<!DOCTYPE html>
<html lang="en">
<head>
<meta charset="utf-8">
<title>Aisle Bloom Bridal Show Flyer</title>
<link rel="stylesheet" href="https://fonts.googleapis.com/css2?family=Lobster&family=Playball&family=Open+Sans:wght@300;400;600;700&display=swap">
<style>
  :root {
    --backdrop: #ecebe7;
    --rose: #d6767c;
    --rose-deep: #c9626a;
    --rose-text: #e98a93;
    --panel: rgba(62, 52, 44, 0.82);
    --cream: #fbf7f2;
    --rule: rgba(255, 255, 255, 0.45);
    --photo-green: #7d8a5e;
    --photo-light: #c9cdb2;
    --photo-gown: #f3f1ec;
  }
  * { margin: 0; padding: 0; box-sizing: border-box; }
  html, body { width: 1200px; height: 1000px; overflow: hidden; }
  body {
    background: var(--backdrop);
    font-family: "Open Sans", sans-serif;
    color: var(--cream);
    position: relative;
  }
  .flyer {
    position: absolute;
    left: 50px;
    top: 130px;
    width: 1100px;
    height: 740px;
    overflow: hidden;
    box-shadow: 0 10px 30px rgba(0,0,0,0.18);
  }
  .bride-photo {
    position: absolute;
    inset: 0;
    background:
      radial-gradient(ellipse 34% 55% at 76% 50%, var(--photo-gown) 0%, rgba(243,241,236,0.85) 45%, rgba(243,241,236,0) 75%),
      radial-gradient(ellipse 14% 16% at 52% 20%, #7a3b25 0%, rgba(122,59,37,0) 100%),
      linear-gradient(110deg, #5f6b45 0%, var(--photo-green) 35%, var(--photo-light) 70%, #e3e0cf 100%);
  }
  .details-panel {
    position: absolute;
    left: 70px;
    top: 110px;
    width: 500px;
    height: 500px;
    background: var(--panel);
    text-align: center;
    padding: 34px 40px 0;
  }
  .show-title {
    font-family: "Lobster", cursive;
    font-size: 84px;
    line-height: 1;
    color: #fff;
  }
  .casting-call {
    margin-top: 12px;
    font-weight: 300;
    font-size: 34px;
    letter-spacing: 1px;
    color: var(--rose-text);
    text-transform: uppercase;
    line-height: 1.1;
  }
  .tagline {
    font-weight: 700;
    font-size: 24px;
    color: var(--rose-text);
    text-transform: uppercase;
    line-height: 1.2;
  }
  .divider { height: 1px; background: var(--rule); margin: 16px 20px; }
  .prize-intro {
    font-size: 15px;
    letter-spacing: 1.5px;
    text-transform: uppercase;
  }
  .prize-amount {
    font-weight: 700;
    font-size: 44px;
    line-height: 1.15;
  }
  .event-date { font-size: 16px; letter-spacing: 0.5px; }
  .venue {
    margin-top: 6px;
    font-weight: 700;
    font-size: 22px;
    line-height: 1.25;
  }
  .giveaway {
    font-family: "Playball", cursive;
    font-size: 30px;
  }
  .coupon-badge {
    position: absolute;
    right: 70px;
    top: 470px;
    width: 130px;
    height: 130px;
  }
  .coupon-text {
    position: absolute;
    inset: 0;
    display: flex;
    flex-direction: column;
    justify-content: center;
    align-items: center;
    text-align: center;
    font-size: 11px;
    line-height: 1.25;
    color: #fff;
  }
  .coupon-text strong { font-size: 17px; }
  .info-band {
    position: absolute;
    left: 0;
    right: 0;
    bottom: 0;
    height: 120px;
    background: var(--rose);
    display: flex;
    align-items: center;
    justify-content: space-between;
    padding: 0 50px;
  }
  .brand-name {
    display: flex;
    align-items: center;
    gap: 14px;
    font-size: 40px;
    font-weight: 300;
    color: var(--cream);
  }
  .brand-dot {
    width: 18px;
    height: 18px;
    border-radius: 50%;
    background: var(--cream);
  }
  .band-credits { text-align: right; line-height: 1.6; }
  .sponsor { font-size: 18px; }
  .tickets { font-size: 15px; font-weight: 600; letter-spacing: 1px; text-transform: uppercase; }
</style>
</head>
<body>
  <section class="flyer">
    <div class="bride-photo" role="img" aria-label="Photo of a bride from behind in a white lace-up gown with a flower crown, holding a bouquet in a soft green garden"></div>

    <div class="details-panel">
      <h1 class="show-title">Bridal Show</h1>
      <p class="casting-call">Open Casting Call</p>
      <p class="tagline">Find Your Forever Gown</p>
      <div class="divider"></div>
      <p class="prize-intro">The first 50 brides will get a chance to win</p>
      <p class="prize-amount">$25,000</p>
      <div class="divider"></div>
      <p class="event-date">Tuesday • September 16th • 6:00-9:00 PM</p>
      <p class="venue">The Lakeside at Marcello's<br>410 Harbor Lane Millbrook, CT</p>
      <div class="divider"></div>
      <p class="giveaway">Honeymoon Cruise Give Away</p>
    </div>

    <div class="coupon-badge">
      <svg width="130" height="130" viewBox="0 0 130 130" aria-hidden="true">
        <polygon fill="var(--rose-deep)" stroke="#fff" stroke-width="2"
          points="127,65 118,75.5 122.3,88.7 109.9,95 108.8,108.8 95,109.9 88.7,122.3 75.5,118 65,127 54.5,118 41.3,122.3 35,109.9 21.2,108.8 20.1,95 7.7,88.7 12,75.5 3,65 12,54.5 7.7,41.3 20.1,35 21.2,21.2 35,20.1 41.3,7.7 54.5,12 65,3 75.5,12 88.7,7.7 95,20.1 108.8,21.2 109.9,35 122.3,41.3 118,54.5"/>
      </svg>
      <p class="coupon-text"><strong>$3 off</strong>admission by<br>using coupon<br>code NP3</p>
    </div>

    <footer class="info-band">
      <div class="brand-name"><span class="brand-dot"></span>Aisle Bloom</div>
      <div class="band-credits">
        <p class="sponsor">Sponsored by Brightbeat Entertainment</p>
        <p class="tickets">Get tickets at aislebloom.com 555-014-2290</p>
      </div>
    </footer>
  </section>
</body>
</html>
```